KT ELECTRICAL SERVICES

I am just setting up on my own as an electrician. I want a 2 sided business card that is eye catching on the front and has skills on the back. I do domestic, commercial and agricultural work.
Inspection and Testing.
Rewires.
Fuseboards.
New builds.
Fault finding.
Free quotations
All work undertaken.
10 years experience.
Registered and insured by VORSEC.
Customer references available on request.
Kevin Tallis. Mob. 07700900461. Home 01632960418.
Email. merrow.kt@postvale.com.
My own unique logo would be nice either electrical related or KT initial related.
After seeing all the designs I prefer something simple but striking. My favourite so far is just black background blue and red writing and is simple but striking. And a KT with something electrical incorporated into it.

Industry/Entity Type

Electrical

Requirements
Must have
• Services and a good logo or graphic.

```html
<!DOCTYPE html>
<html lang="en">
<head>
<meta charset="utf-8">
<title>KT Electrical Services – Business Card</title>
<link rel="stylesheet" href="https://fonts.googleapis.com/css2?family=Source+Sans+3:wght@400;600;700&family=Tinos&display=swap">
<style>
  :root {
    --backdrop: #4b423d;
    --card: #1b1b1c;
    --card-edge: #2a2a2b;
    --blue: #2f6cc0;
    --red: #e0141b;
    --white: #f2f2f2;
    --muted: #8a8a8a;
  }
  * { box-sizing: border-box; margin: 0; padding: 0; }
  html, body { width: 1200px; height: 812px; overflow: hidden; }
  body {
    background: var(--backdrop);
    font-family: "Source Sans 3", "Source Sans Pro", sans-serif;
    position: relative;
  }
  .card {
    position: absolute;
    width: 540px;
    height: 310px;
    background: var(--card);
    border: 1px solid var(--card-edge);
    border-radius: 6px;
    box-shadow: 0 14px 30px rgba(0,0,0,.45);
  }
  .card--back { left: 35px; top: 250px; }
  .card--front { left: 625px; top: 250px; }

  /* Back: services */
  .services-title {
    position: absolute; left: 30px; top: 34px;
    color: var(--blue); font-weight: 700; font-size: 21px;
  }
  .services-list {
    position: absolute; left: 110px; top: 88px;
    list-style: none; color: var(--white); font-size: 17px; line-height: 27px;
  }
  .services-list li { display: flex; align-items: center; gap: 9px; }
  .services-list li::before {
    content: ""; width: 7px; height: 7px; background: var(--red); flex: none;
  }

  /* Front: identity */
  .brand {
    position: absolute; left: 150px; top: 78px;
    display: flex; align-items: center; gap: 14px;
  }
  .brand-mark { width: 26px; height: 26px; background: var(--blue); }
  .brand-name {
    font-family: "Tinos", serif; color: var(--red); font-size: 32px; line-height: 1.1;
  }
  .owner {
    position: absolute; left: 40px; top: 208px;
    color: var(--blue); font-weight: 700; font-size: 24px;
  }
  .divider {
    position: absolute; left: 222px; top: 196px; width: 1px; height: 62px;
    background: var(--muted);
  }
  .contacts {
    position: absolute; left: 240px; top: 192px;
    list-style: none; color: var(--white); font-size: 16px; line-height: 24px;
  }
  .contacts li { display: flex; align-items: center; gap: 9px; }
  .contacts svg { width: 12px; height: 12px; fill: var(--blue); flex: none; }
</style>
</head>
<body>
  <section class="card card--back" aria-label="Card back: services">
    <h2 class="services-title">Domestic, Commercial and Agricultural work.</h2>
    <ul class="services-list">
      <li>Inspection and testing.</li>
      <li>Fuseboards.</li>
      <li>Full and part rewires.</li>
      <li>Fault finding.</li>
      <li>Free quotations.</li>
      <li>All work guaranteed and insured by VORSEC.</li>
    </ul>
  </section>

  <section class="card card--front" aria-label="Card front: contact">
    <div class="brand">
      <span class="brand-mark"></span>
      <span class="brand-name">KT Electrical Services</span>
    </div>
    <p class="owner">Kevin Tallis</p>
    <span class="divider"></span>
    <ul class="contacts">
      <li>
        <svg viewBox="0 0 12 12" aria-hidden="true"><path d="M2.5 1 L4.5 1 L5.3 3.6 L4 4.6 Q5 7 7.4 8 L8.4 6.7 L11 7.5 L11 9.5 Q11 11 9.5 11 Q1 10 1 2.5 Q1 1 2.5 1Z"/></svg>
        01632960418
      </li>
      <li>
        <svg viewBox="0 0 12 12" aria-hidden="true"><path d="M3 0.5 H9 V11.5 H3Z M4 1.8 V9.2 H8 V1.8Z M5.4 10 H6.6 V10.8 H5.4Z" fill-rule="evenodd"/></svg>
        07700900461
      </li>
      <li>
        <svg viewBox="0 0 12 12" aria-hidden="true"><path d="M0.5 2.5 H11.5 V9.5 H0.5Z M1.5 3.3 L6 6.6 L10.5 3.3" /></svg>
        merrow.kt@postvale.com
      </li>
    </ul>
  </section>
</body>
</html>
```